Business Card Design Project

Hi. We need a new business card for Brightfield Partners, a consultancy that helps people with online marketing strategy and solutions.

We have a new logo and now need the info presented - front and back of business card.

FRONT

Logo

Online strategy, consulting and coaching
Varlo Admarket consulting
Search Engine Optimisation
Internet Lead Generation
Domain name broking

BACK

Tom Bradwell-Jones
+ 61 83215 9076
+ 61 (0) 418 536 207
tom@brightfieldpartners.com.au
www.brightfieldpartners.com.au

Talkora: tombradwelljones
PO Box 312, South Perth, Western Australia 6951

Target Market(s)

Business owners, corporates

Industry/Entity Type

Marketing

Requirements
Must have
• double sided
size: 86 x 54mm
supplied as one pdf with crop marks shown (+- 1mm, with 2-3 mm bleed)

```html
<!DOCTYPE html>
<html lang="en">
<head>
<meta charset="utf-8">
<title>Brightfield Partners – Business Card</title>
<link rel="stylesheet" href="https://fonts.googleapis.com/css2?family=Arimo:wght@400;700&display=swap">
<style>
  :root {
    --brand-blue: #1f4f8f;
    --name-blue: #2b5c9b;
    --brand-orange: #f7901e;
    --soft-grey: #d1d3d4;
    --card-white: #ffffff;
    --card-edge: #111111;
    --page-bg: #ffffff;
  }
  * { margin: 0; padding: 0; box-sizing: border-box; }
  html, body {
    width: 1200px; height: 1200px; overflow: hidden;
    background: var(--page-bg);
    font-family: "Arimo", Arial, sans-serif;
  }
  .canvas { position: relative; width: 1200px; height: 1200px; }
  .card {
    position: absolute; left: 180px; width: 840px; height: 482px;
    background: var(--card-white);
    border: 2px solid var(--card-edge);
    overflow: hidden;
  }
  .card--front { top: 28px; }
  .card--back { top: 682px; }
  .card__rings { position: absolute; inset: 0; width: 100%; height: 100%; }
  .ring-band { fill: var(--brand-orange); }
  .ring-gap { fill: var(--card-white); }
  .ring-core { fill: var(--soft-grey); }

  .brand {
    position: absolute; left: 300px; top: 62px;
    display: flex; align-items: center; gap: 20px;
  }
  .brand__dot {
    width: 74px; height: 74px; border-radius: 50%;
    background: var(--brand-orange); flex: none;
  }
  .brand__name {
    color: var(--brand-blue); font-weight: 700;
    font-size: 62px; line-height: 1.02; letter-spacing: -1px;
  }
  .brand__url {
    position: absolute; right: 70px; top: 272px;
    color: var(--brand-blue); font-weight: 700;
    font-size: 17px; letter-spacing: 3px;
  }
  .services {
    position: absolute; right: 74px; top: 316px;
    list-style: none; text-align: right;
    color: var(--brand-blue); font-size: 19px; line-height: 26.5px;
  }

  .person {
    position: absolute; left: 48px; top: 58px;
    color: var(--name-blue); font-weight: 700; font-size: 42px;
  }
  .contact {
    position: absolute; left: 48px; top: 148px;
    color: var(--brand-orange); font-size: 23px; line-height: 32px;
    font-style: normal;
  }
  .contact__group + .contact__group { margin-top: 32px; }
</style>
</head>
<body>
<main class="canvas">

  <section class="card card--front" aria-label="Card front">
    <svg class="card__rings" viewBox="0 0 840 482" aria-hidden="true">
      <circle class="ring-band" cx="-24" cy="248" r="384"/>
      <circle class="ring-gap" cx="-24" cy="248" r="276"/>
      <circle class="ring-core" cx="-14" cy="221" r="146"/>
    </svg>
    <div class="brand">
      <span class="brand__dot"></span>
      <span class="brand__name">Brightfield<br>Partners</span>
    </div>
    <p class="brand__url">brightfieldpartners.com.au</p>
    <ul class="services">
      <li>Online strategy, consulting and coaching</li>
      <li>Varlo Admarket consulting</li>
      <li>Search engine optimisation</li>
      <li>Internet lead generation</li>
      <li>Domain name broking</li>
    </ul>
  </section>

  <section class="card card--back" aria-label="Card back">
    <svg class="card__rings" viewBox="0 0 840 482" aria-hidden="true">
      <circle class="ring-band" cx="862" cy="239" r="376"/>
      <circle class="ring-gap" cx="862" cy="239" r="256"/>
      <circle class="ring-core" cx="862" cy="239" r="144"/>
    </svg>
    <h1 class="person">Tom Bradwell-Jones</h1>
    <address class="contact">
      <div class="contact__group">
        <div>+ 61 83215 9076</div>
        <div>+ 61 (0) 418 536 207</div>
        <div>tom@brightfieldpartners.com.au</div>
        <div>www.brightfieldpartners.com.au</div>
      </div>
      <div class="contact__group">
        <div>Talkora: tombradwelljones</div>
      </div>
      <div class="contact__group">
        <div>PO Box 312, South Perth</div>
        <div>Western Australia 6951</div>
      </div>
    </address>
  </section>

</main>
</body>
</html>
```